Truck Wrap Design

Project Scope
Design a full vehicle wrap for a box truck (Pantech-style) that elevates the brand identity of Larkfield Signs and Wraps. The design should reflect the fun, approachable personality of the brand while delivering a bold and professional visual impact that turns heads in traffic.
⸻
Design Goals
• Maintain the character-driven style shown in the initial mockup (squeegee mascot with a heat gun).
• Preserve the brand colour palette (deep navy, magenta, teal blue).
• Use a wavy, flowing background as seen in the mockup — but refine it with more defined lines or structured layering, inspired by BrightMarrow’s confident composition.
• Ensure high visibility of the brand name and contact number from a distance.
• Vehicle should be recognisable and consistent with other brand assets (uniforms, cards, hats).
• Create front, side, and rear panel views.
⸻
Creative Style & Tone
• Playful but sharp.
• Friendly and energetic with a hint of retro charm (like BrightMarrow’s Tidewell Co and Snug Otter).
• Character-forward branding (the mascot should have presence and personality, not be lost in background noise).
⸻
Design Elements to Include
• Logo – prominent on all sides
•. Mascot – showcased clearly, ideally interacting with the background or layout
• Phone number – clearly legible and consistently placed
• Slogan or service callout (optional) – such as “Vehicle Wraps, LED Signs & More”
• Website URL – small but readable near rear or base panel
• Colours – Stick to current palette: Navy, Magenta, Teal, White
• Flowing background – evolve current wave style with sharper edges or layered “ribbons”
• Typography – Clean, bold fonts. Avoid thin script or overly quirky type.
⸻
Avoid
• Overcrowding the design with too many service listings
• Heavy gradients that muddy the clarity from afar
• Muted colours — we want contrast and pop

```html
<!DOCTYPE html>
<html lang="en">
<head>
<meta charset="utf-8">
<title>Larkfield Signs and Wraps – Truck Wrap Panels</title>
<link href="https://fonts.googleapis.com/css2?family=Fredoka:wght@600;700&family=Sansita:wght@800&display=swap" rel="stylesheet">
<style>
  :root {
    --backdrop: #a7a7a7;
    --teal: #13707f;
    --teal-light: #3aa8c9;
    --navy: #1b2a3a;
    --magenta: #bf2f74;
    --purple: #6b3b7c;
    --pink: #ea3f93;
    --white: #ffffff;
  }
  html, body { margin: 0; padding: 0; overflow: hidden; }
  body { background: var(--backdrop); }
  .canvas {
    position: relative;
    width: 775px;
    height: 1200px;
    overflow: hidden;
    background: var(--backdrop);
  }
  .panel { position: absolute; display: block; }
  .panel--side-left  { left: 40px;  top: 60px;  width: 695px; height: 262px; }
  .panel--side-right { left: 40px;  top: 380px; width: 695px; height: 262px; }
  .panel--front      { left: 55px;  top: 720px; width: 300px; height: 130px; }
  .panel--rear       { left: 420px; top: 720px; width: 300px; height: 320px; }

  .wrap-bg { fill: var(--teal); }
  .wave-navy { fill: var(--navy); }
  .wave-purple { fill: var(--purple); }
  .wave-magenta { fill: var(--magenta); }
  .wave-line { fill: none; stroke: var(--navy); stroke-width: 10; stroke-linecap: round; }

  .outlined { paint-order: stroke fill; stroke: var(--navy); stroke-linejoin: round; }
  .phone { font-family: "Fredoka", sans-serif; font-weight: 700; fill: var(--white); stroke-width: 7; }
  .brand-name { font-family: "Fredoka", sans-serif; font-weight: 700; fill: var(--white); stroke-width: 8; }
  .brand-tagline { font-family: "Fredoka", sans-serif; font-weight: 600; fill: var(--white); stroke-width: 6; letter-spacing: 1px; }
  .services { font-family: "Sansita", sans-serif; font-weight: 800; fill: var(--white); stroke-width: 7; }
  .web-address { font-family: "Sansita", sans-serif; font-weight: 800; fill: var(--pink); paint-order: stroke fill; stroke: var(--white); stroke-width: 5; stroke-linejoin: round; }
</style>
</head>
<body>
<div class="canvas">

  <svg width="0" height="0" style="position:absolute" aria-hidden="true">
    <defs>
      <linearGradient id="mascot-fill" x1="0" y1="0" x2="0" y2="1">
        <stop offset="0" stop-color="#3aa8c9"/>
        <stop offset="1" stop-color="#2b86a8"/>
      </linearGradient>
    </defs>
  </svg>

  <!-- Driver side panel -->
  <svg class="panel panel--side-left" viewBox="0 0 695 262" aria-label="Driver side box panel">
    <rect class="wrap-bg" width="695" height="262"/>
    <path class="wave-purple" d="M420 0 C520 60 600 20 695 70 L695 0 Z"/>
    <path class="wave-navy" d="M0 40 C60 10 120 60 90 130 C70 190 200 210 330 200 C470 190 520 120 600 150 C650 170 680 120 695 110 L695 200 C600 230 480 250 340 240 C180 232 40 230 0 200 Z"/>
    <path class="wave-magenta" d="M0 230 C120 200 260 255 400 225 C520 200 600 235 695 205 L695 262 L0 262 Z"/>
    <path class="wave-line" d="M20 60 C70 40 60 150 140 170"/>
    <rect x="470" y="18" width="170" height="180" rx="30" fill="url(#mascot-fill)" role="img" aria-label="Squeegee mascot character holding a heat gun and giving a thumbs up"/>
    <text class="phone outlined" x="40" y="72" font-size="34" transform="rotate(-3 40 72)">0400 555 012</text>
    <text class="brand-name outlined" x="92" y="150" font-size="70" transform="rotate(-4 92 150)">Larkfield</text>
    <text class="brand-tagline outlined" x="145" y="192" font-size="20" transform="rotate(-4 145 192)">SIGNS AND WRAPS</text>
    <text class="services outlined" x="255" y="212" font-size="25" transform="rotate(-4 255 212)">Vehicle Wraps</text>
    <text class="services outlined" x="272" y="242" font-size="25" transform="rotate(-4 272 242)">LED Signs More</text>
    <text class="web-address" x="522" y="242" font-size="17" transform="rotate(-6 522 242)">LarkfieldWraps.com</text>
  </svg>

  <!-- Passenger side panel -->
  <svg class="panel panel--side-right" viewBox="0 0 695 262" aria-label="Passenger side box panel">
    <rect class="wrap-bg" width="695" height="262"/>
    <path class="wave-purple" d="M0 70 C80 20 160 60 260 0 L0 0 Z"/>
    <path class="wave-navy" d="M695 40 C640 10 580 70 610 140 C630 200 480 215 350 205 C220 195 170 120 90 150 C40 170 15 120 0 110 L0 205 C110 235 230 250 360 242 C520 232 640 230 695 205 Z"/>
    <path class="wave-magenta" d="M0 210 C120 240 280 200 420 232 C540 255 620 215 695 230 L695 262 L0 262 Z"/>
    <path class="wave-line" d="M675 60 C625 40 640 150 560 172"/>
    <rect x="60" y="18" width="175" height="172" rx="30" fill="url(#mascot-fill)" role="img" aria-label="Squeegee mascot character holding a heat gun and giving a thumbs up"/>
    <text class="phone outlined" x="385" y="60" font-size="34" transform="rotate(3 385 60)">0400 555 012</text>
    <text class="brand-name outlined" x="292" y="140" font-size="70" transform="rotate(3 292 140)">Larkfield</text>
    <text class="brand-tagline outlined" x="325" y="182" font-size="20" transform="rotate(3 325 182)">SIGNS AND WRAPS</text>
    <text class="services outlined" x="190" y="214" font-size="25" transform="rotate(3 190 214)">Vehicle Wraps</text>
    <text class="services outlined" x="205" y="244" font-size="25" transform="rotate(3 205 244)">LED Signs More</text>
    <text class="web-address" x="22" y="224" font-size="17" transform="rotate(5 22 224)">LarkfieldWraps.com</text>
  </svg>

  <!-- Front header panel -->
  <svg class="panel panel--front" viewBox="0 0 300 130" aria-label="Front header panel above the cab">
    <rect class="wrap-bg" width="300" height="130"/>
    <path class="wave-purple" d="M170 0 C220 30 260 10 300 40 L300 0 Z"/>
    <path class="wave-navy" d="M0 70 C60 110 150 90 220 100 C260 105 285 80 300 70 L300 115 L0 115 Z"/>
    <path class="wave-magenta" d="M0 112 C80 95 200 125 300 100 L300 130 L0 130 Z"/>
    <text class="phone outlined" x="45" y="50" font-size="26" transform="rotate(-3 45 50)">0400 555 012</text>
    <text class="web-address" x="110" y="76" font-size="16" transform="rotate(-4 110 76)">LarkfieldWraps.com</text>
  </svg>

  <!-- Rear door panel -->
  <svg class="panel panel--rear" viewBox="0 0 300 320" aria-label="Rear roller door panel">
    <rect class="wrap-bg" width="300" height="320"/>
    <path class="wave-purple" d="M120 60 C180 20 240 40 300 10 L300 90 C240 70 180 90 120 60 Z"/>
    <path class="wave-navy" d="M0 150 C50 200 130 170 200 200 C250 220 280 190 300 180 L300 270 C220 250 120 290 0 260 Z"/>
    <path class="wave-magenta" d="M0 265 C100 245 200 285 300 255 L300 320 L0 320 Z"/>
    <rect x="196" y="30" width="94" height="150" rx="22" fill="url(#mascot-fill)" role="img" aria-label="Squeegee mascot character holding a heat gun and giving a thumbs up"/>
    <text class="phone outlined" x="22" y="92" font-size="22" transform="rotate(-3 22 92)">0400 555 012</text>
    <text class="brand-name outlined" x="14" y="150" font-size="40" transform="rotate(-5 14 150)">Larkfield</text>
    <text class="brand-tagline outlined" x="46" y="176" font-size="14" transform="rotate(-5 46 176)">SIGNS AND WRAPS</text>
    <text class="services outlined" x="48" y="225" font-size="26" transform="rotate(-5 48 225)">Vehicle Wraps</text>
    <text class="services outlined" x="40" y="258" font-size="26" transform="rotate(-5 40 258)">LED Signs More</text>
    <text class="web-address" x="110" y="292" font-size="18" transform="rotate(-6 110 292)">LarkfieldWraps.com</text>
  </svg>

</div>
</body>
</html>
```